Label Design for Saffron Company

We need a label design that is unique for our container. The item inside the container is Saffron, and it is 5g in weigh. We need on the label our logo, the weight and quality. Here is the exactly what we want. We want the background to be black for the label and the design to present royalty, and premium quality.

Premium Quality
Grade A+ Premium Saffron
100% Natural and Pure
www.QamarivaSpice.com

Target Market(s)

Everyone

Requirements
Must have
• Black background, golden border design. Unique design, that show premium and royalty.
Nice to have
• The logo is attached with transparent background so you can show exactly how things look like.
Should not have
• different colors that are not part of the logo.

```html
<!DOCTYPE html>
<html lang="en">
<head>
<meta charset="utf-8">
<title>Qamariva Spice – Saffron Lid Label</title>
<link rel="stylesheet" href="https://fonts.googleapis.com/css2?family=Cinzel:wght@400;700&family=Poppins:wght@400&display=swap">
<style>
  :root {
    --page: #ffffff;
    --label-black: #0a0806;
    --gold-deep: #b8892a;
    --gold-mid: #e2c565;
    --gold-light: #f9f0b2;
    --rim-dark: #8a5a14;
    --rim-light: #f6d978;
    --dot-gold: #e6b84a;
    --ink: #14100a;
  }
  html, body {
    margin: 0;
    padding: 0;
    width: 1200px;
    height: 2398px;
    overflow: hidden;
    background: var(--page);
  }
  .canvas {
    display: block;
    width: 1200px;
    height: 2398px;
  }
  .brand-name {
    font-family: "Cinzel", serif;
    font-weight: 400;
    fill: var(--ink);
  }
  .headline {
    font-family: "Cinzel", serif;
    font-weight: 700;
    font-size: 64px;
    fill: var(--ink);
  }
  .spec-line {
    font-family: "Poppins", sans-serif;
    font-weight: 400;
    font-size: 29px;
    fill: var(--ink);
  }
  .web-address {
    font-family: "Cinzel", serif;
    font-weight: 400;
    font-size: 40px;
    fill: var(--ink);
    letter-spacing: 1px;
  }
  .brand-square {
    fill: none;
    stroke: var(--ink);
    stroke-width: 5;
  }
  .outer-disc { fill: var(--label-black); }
  .dot-ring {
    fill: none;
    stroke: var(--dot-gold);
    stroke-width: 11;
    stroke-linecap: round;
  }
</style>
</head>
<body>
<svg class="canvas" viewBox="0 0 1200 2398" xmlns="http://www.w3.org/2000/svg" xmlns:xlink="http://www.w3.org/1999/xlink">
  <defs>
    <linearGradient id="gold-face" x1="0" y1="0" x2="1" y2="0">
      <stop offset="0" stop-color="var(--gold-deep)"/>
      <stop offset="0.45" stop-color="var(--gold-light)"/>
      <stop offset="0.6" stop-color="var(--gold-light)"/>
      <stop offset="1" stop-color="var(--gold-deep)"/>
    </linearGradient>
    <linearGradient id="gold-rim" x1="0" y1="0" x2="1" y2="1">
      <stop offset="0" stop-color="var(--rim-light)"/>
      <stop offset="0.5" stop-color="var(--rim-dark)"/>
      <stop offset="1" stop-color="var(--rim-light)"/>
    </linearGradient>
    <path id="address-arc" d="M -372 0 A 372 372 0 0 0 372 0"/>

    <g id="lid-label">
      <circle class="outer-disc" r="465"/>
      <circle class="dot-ring" r="438" pathLength="76" stroke-dasharray="0 1"/>
      <circle r="412" fill="url(#gold-rim)"/>
      <circle r="396" fill="url(#gold-face)"/>

      <rect class="brand-square" x="-68" y="-296" width="136" height="136" rx="16"/>
      <text class="brand-name" x="0" y="-105" text-anchor="middle" font-size="38" letter-spacing="8">QAMARIVA</text>
      <text class="brand-name" x="0" y="-30" text-anchor="middle" font-size="66" letter-spacing="2">SPICE</text>

      <text class="headline" x="0" y="76" text-anchor="middle">Premium Quality</text>
      <text class="spec-line" x="0" y="139" text-anchor="middle">GRADE A+</text>
      <text class="spec-line" x="0" y="191" text-anchor="middle">PREMIUM SAFFRON</text>
      <text class="spec-line" x="0" y="244" text-anchor="middle">100% NATRUAL AND PURE</text>
      <text class="spec-line" x="0" y="302" text-anchor="middle">5G</text>

      <text class="web-address">
        <textPath xlink:href="#address-arc" href="#address-arc" startOffset="50%" text-anchor="middle">www.QamarivaSpice.com</textPath>
      </text>
    </g>
  </defs>

  <use class="label-top" href="#lid-label" xlink:href="#lid-label" transform="translate(600 493) scale(0.95)"/>
  <use class="label-bottom" href="#lid-label" xlink:href="#lid-label" transform="translate(600 1795)"/>
</svg>
</body>
</html>
```